Swimming Pool Service business card needed!!!! Please

Hi Everyone! Thanks for looking at my contest. I PROMISE to provide excellent feedback during this process.

I am starting a new swimming pool cleaning business in San Diego, California and would like your help in making a business card for me.

I like easy to read, classy and sophisticated.

I am having a website designed and I'm looking for it to have pictures of really clean & clear pools.

I really like the blue on white color format, but open to other colors.

I do not have a logo, but the name of my company is GLIMMERTIDE POOL SERVICE.

My tag line is: Pools so clean, you can see yourself "in" them. (does not need to have the quotes around "in"...maybe just italics for this word IN?) You decide for me.

I would like to have a logo designed that incorporates some sort of easy to read letters. I do not want cursive (handwriting) letters. I thought about having a "reflection" of letters (mirror image), but think that this will be hard to read from far away. Maybe you can surprise me and come up with an idea that works using the a mirror image....but I'm not sure. I was leaning toward plain old BLOCK letters as I think it would be easy to read on my truck.

I would like to have the NAQTR and WBK logos on the back of the card. I have attached those two as files. You can put other things on the back as well, but I need these two logos on there. Or maybe put them on the front of the card if you have a better idea for the back of the card! :-)

Maybe blue on the back of the card and white on the front of the card? I don't know, I'm just thinking out loud.

I had another card done awhile ago called HARBORLINE TEES. I have uploaded a copy of that card for your reference. I don't want this card to be the same as my new company is a swimming pool cleaning company, but I wanted you to see what I liked in the past.

THANK YOU!!!!
Updates

Reason: Partner out of town and want their feedback....so need more time to decide and designs still coming in.

Industry/Entity Type

Business

Contact Information for Business Card

GLIMMERTIDE POOL SERVICE
Dale Wexby
Owner
4817 Quarry Bend Ave. #512
San Diego, CA 92417
858-291-6083
www.glimmertidepoolservice.example

Font styles to use
Sans Serif

Colors
0255a3
3176b5
ffffff

Requirements
Nice to have
• Some things to (possibly) add to back of card (in no particular order)
• WBK logo
• NAQTR logo
• Free Estimates
• Residential and Commercial Services
• Equipment Repairs
• Saltwater Systems
• Licensed, Bonded, Insured
• Family Owned and Operated
• No Contracts
• =======================
• Check out the FolioMint business card that i attached.
• i think they did this using a chrome overlay.
• Can any of you guys design that? or is that done at my printer?
• ==================
Should not have
• Hi Designers-
• The first round of cards came back and let's stay away from the light blue (powder blue) color. I don't like the look of it on the business cards.
• Also, the pool company JPG's that I attached are other logos of pool companies that I liked. I don't want them to be on my card. The only logos that should be on my card are the one you are going to come up with for my company, the WBK logo and the NAQTR logo.
• Lastly, no vertical cards and no split cards (logo on left, contact info on right side).
• Thanks much!

```html
<!DOCTYPE html>
<html lang="en">
<head>
<meta charset="utf-8">
<title>Glimmertide Pool Service – Business Card</title>
<link href="https://fonts.googleapis.com/css2?family=Roboto:ital,wght@0,400;0,700;0,900;1,400&display=swap" rel="stylesheet">
<style>
  :root {
    --page: #eceef1;
    --card: #ffffff;
    --navy: #0255a3;
    --blue: #0255a3;
    --mid: #3176b5;
    --ink: #3f63b0;
    --badge: #3176b5;
    --badge-ring: #0255a3;
  }
  * { box-sizing: border-box; margin: 0; padding: 0; }
  html, body { width: 1200px; height: 902px; overflow: hidden; }
  body {
    background: var(--page);
    font-family: "Roboto", Arial, sans-serif;
    position: relative;
  }
  .card {
    position: absolute;
    width: 560px;
    height: 320px;
    background: var(--card);
    overflow: hidden;
    box-shadow: 0 6px 18px rgba(20, 40, 80, 0.18);
  }
  .card-front { left: 70px; top: 80px; }
  .card-back { left: 570px; top: 500px; }
  .card-wave { position: absolute; inset: 0; width: 100%; height: 100%; }

  .brand {
    position: absolute;
    display: flex;
    align-items: center;
    gap: 12px;
  }
  .brand-dot {
    width: 26px; height: 26px;
    border-radius: 50%;
    background: var(--mid);
    flex: none;
  }
  .brand-name {
    color: var(--navy);
    font-weight: 900;
    letter-spacing: 0.5px;
    line-height: 1;
    white-space: nowrap;
  }
  .card-front .brand { left: 0; right: 0; top: 92px; justify-content: center; }
  .card-front .brand-name { font-size: 30px; }
  .tagline {
    position: absolute;
    left: 0; right: 0;
    top: 138px;
    text-align: center;
    color: var(--mid);
    font-size: 15px;
  }
  .tagline em { font-style: italic; font-weight: 700; }

  .card-back .brand { left: 28px; top: 112px; gap: 8px; }
  .card-back .brand-dot { width: 16px; height: 16px; }
  .card-back .brand-name { font-size: 18px; }

  .contact {
    position: absolute;
    left: 40px;
    top: 160px;
    list-style: none;
    color: var(--ink);
    font-size: 13px;
    line-height: 1.35;
  }
  .contact li { display: flex; align-items: flex-start; gap: 9px; margin-bottom: 3px; white-space: nowrap; }
  .contact svg { width: 12px; height: 12px; margin-top: 2px; flex: none; fill: var(--ink); }

  .badges {
    position: absolute;
    left: 320px;
    top: 36px;
    display: flex;
    gap: 16px;
  }
  .badge {
    width: 50px; height: 50px;
    border-radius: 50%;
    background: var(--badge);
    border: 4px solid var(--badge-ring);
  }

  .owner {
    position: absolute;
    right: 24px;
    bottom: 96px;
    text-align: right;
    color: #ffffff;
  }
  .owner-name { font-size: 20px; font-weight: 700; }
  .owner-title { font-size: 11px; }
</style>
</head>
<body>

<section class="card card-front" aria-label="Card front">
  <svg class="card-wave" viewBox="0 0 560 320" preserveAspectRatio="none" aria-hidden="true">
    <path d="M0,205 C150,265 320,255 560,150 L560,320 L0,320 Z" fill="var(--mid)"/>
    <path d="M0,222 C160,280 340,262 560,168 L560,320 L0,320 Z" fill="var(--blue)"/>
  </svg>
  <div class="brand">
    <span class="brand-dot"></span>
    <span class="brand-name">GLIMMERTIDE POOL SERVICE</span>
  </div>
  <p class="tagline">Pools so clean, you can see yourself <em>in</em> them.</p>
</section>

<section class="card card-back" aria-label="Card back">
  <svg class="card-wave" viewBox="0 0 560 320" preserveAspectRatio="none" aria-hidden="true">
    <path d="M455,0 L560,0 L560,320 L225,320 C310,300 370,255 410,200 C455,140 485,60 455,0 Z" fill="var(--mid)"/>
    <path d="M470,0 L560,0 L560,320 L250,320 C335,302 392,258 430,205 C470,148 498,62 470,0 Z" fill="var(--blue)"/>
  </svg>

  <div class="badges" aria-label="Certification badges">
    <span class="badge" role="img" aria-label="NAQTR membership badge"></span>
    <span class="badge" role="img" aria-label="WBK certification badge"></span>
  </div>

  <div class="brand">
    <span class="brand-dot"></span>
    <span class="brand-name">GLIMMERTIDE POOL SERVICE</span>
  </div>

  <ul class="contact">
    <li>
      <svg viewBox="0 0 24 24"><path d="M6.6 10.8a15.1 15.1 0 0 0 6.6 6.6l2.2-2.2a1 1 0 0 1 1-.25 11.4 11.4 0 0 0 3.6.57 1 1 0 0 1 1 1V20a1 1 0 0 1-1 1A17 17 0 0 1 3 4a1 1 0 0 1 1-1h3.5a1 1 0 0 1 1 1c0 1.25.2 2.45.57 3.57a1 1 0 0 1-.25 1z"/></svg>
      <span>858-291-6083</span>
    </li>
    <li>
      <svg viewBox="0 0 24 24"><path d="M12 2a10 10 0 1 0 0 20 10 10 0 0 0 0-20zm0 2a8 8 0 0 1 7.7 6H4.3A8 8 0 0 1 12 4zm-7.7 10h15.4A8 8 0 0 1 4.3 14z"/></svg>
      <span>www.glimmertidepoolservice.example</span>
    </li>
    <li>
      <svg viewBox="0 0 24 24"><path d="M12 2a7 7 0 0 0-7 7c0 5.2 7 13 7 13s7-7.8 7-13a7 7 0 0 0-7-7zm0 9.5A2.5 2.5 0 1 1 12 6.5a2.5 2.5 0 0 1 0 5z"/></svg>
      <span>4817 Quarry Bend Ave. #512<br>San Diego, CA 92417</span>
    </li>
  </ul>

  <div class="owner">
    <div class="owner-name">Dale Wexby</div>
    <div class="owner-title">Owner</div>
  </div>
</section>

</body>
</html>
```